Social Media Graphics - Copperfield Loop

Create 6-7 individual social media graphics (square size) to encourage folks to join our online course, using either of the text below (only one set of text per graphic:

The Lantern Ridge Method
How to Create a 7-Figure Business From Scratch
Sign Up Today!

Or

The Lantern Ridge Method
Fast-track Your Way to a Multi-Million Business!
Sign Up Today!

For the color scheme of the graphics, use 1 or 2 colors in the color palette attached; or use any colors that look nice with their outfits; AVOID using red, white and blue altogether because it will look like an Independence Day (4th of July) graphic and we don’t want that; make sure the graphics appeal to both men and women

Make sure each graphic contains 1 of the 2 pics attached; and make sure one of the graphics is all TEXT only.

Target Market(s)

men and women looking to make more money

Industry/Entity Type

entrepreneurship

Requirements
Must have
• see the text document attached
Nice to have
• We are open to a nice color design; the color palette colors are not required, especially we don't want red, white and blue used together
Should not have
• AVOID using red, white and blue altogether because it will look like an Independence Day (4th of July) graphic and we dont want that

```html
<!DOCTYPE html>
<html lang="en">
<head>
<meta charset="utf-8">
<title>Copperfield Loop – The Lantern Ridge Method social graphics</title>
<link href="https://fonts.googleapis.com/css2?family=Anton&family=Oswald:wght@500;600;700&family=Montserrat:ital,wght@0,800;0,900;1,500&display=swap" rel="stylesheet">
<style>
  :root{
    --bg:#eceef0;
    --black:#000;
    --white:#fff;
    --red:#d31f2e;
    --gold:#d3a02a;
    --gold-deep:#b98a24;
    --gold-light:#f5e6a0;
    --navy:#141640;
    --gold-sheen:linear-gradient(90deg,#b8862a 0%,#f6e7a1 35%,#c9972e 65%,#f2dc8a 100%);
  }
  *{box-sizing:border-box;margin:0;padding:0}
  html,body{width:1200px;height:792px;overflow:hidden;background:var(--bg)}
  .canvas{position:relative;width:1200px;height:792px;background:var(--bg)}
  .tile{position:absolute;width:349px;height:349px;overflow:hidden;background:var(--black);box-shadow:0 4px 10px rgba(0,0,0,.18)}
  .t1{left:54px;top:36px}.t2{left:426px;top:36px}.t3{left:798px;top:36px}
  .t4{left:54px;top:408px}.t5{left:426px;top:408px}.t6{left:798px;top:408px}
  .abs{position:absolute}
  .photo{position:absolute}
  .btn{position:absolute;font-family:'Oswald',sans-serif;font-weight:600;line-height:1;display:flex;align-items:center;justify-content:center;border-radius:3px;white-space:nowrap;padding:0 6px}
  .btn-red{background:var(--red);color:var(--white)}
  .btn-gold{background:var(--gold-sheen);color:var(--black)}
  .cursor{position:absolute;width:13px;height:17px}
  .gold-text{background:var(--gold-sheen);-webkit-background-clip:text;background-clip:text;color:transparent}
  .cond{font-family:'Anton',sans-serif;line-height:1;white-space:nowrap}
  .oswald{font-family:'Oswald',sans-serif;line-height:1;white-space:nowrap}
  .mont{font-family:'Montserrat',sans-serif;font-weight:900;line-height:1;white-space:nowrap}

  /* tile 1 */
  .t1 .kicker{left:0;width:349px;top:22px;text-align:center;font-size:20px;color:var(--black);font-family:'Oswald',sans-serif;font-weight:600}
  .t1 .h-fast{left:0;width:349px;top:78px;text-align:center;font-size:54px;color:var(--white)}
  .t1 .h-way{left:0;width:349px;top:134px;text-align:center;font-size:33px;font-family:'Oswald',sans-serif;font-weight:500;color:var(--gold)}
  .t1 .h-multi{left:0;width:349px;top:168px;text-align:center;font-size:50px;color:var(--white)}
  .t1 .h-biz{left:0;width:349px;top:220px;text-align:center;font-size:60px;color:var(--gold)}

  /* tile 2 */
  .t2 .the{left:37px;top:30px;font-size:18px;color:var(--white)}
  .t2 .name{left:35px;top:52px;font-size:29px;letter-spacing:-1px}
  .t2 .method{right:50px;top:110px;font-size:17px;color:var(--white);font-weight:800;letter-spacing:1px}
  .t2 .sub{right:25px;top:229px;text-align:right;font-size:15px;color:var(--white);line-height:1.2}

  /* tile 3 */
  .t3 .panel{left:38px;top:28px;width:268px;height:261px;background:var(--white);border-radius:10px}
  .t3 .the{left:50px;top:50px;font-size:38px;color:var(--black)}
  .t3 .word{left:50px;font-size:48px;color:var(--red);letter-spacing:-1px}
  .t3 .method{right:58px;top:216px;font-size:40px;color:var(--black)}
  .t3 .sub{left:40px;top:306px;font-family:'Montserrat',sans-serif;font-style:italic;font-weight:500;font-size:11px;color:var(--white);line-height:1.4}

  /* tile 4 */
  .t4 .the{font-size:18px;color:var(--white);transform:rotate(-90deg);transform-origin:left top;top:70px;left:26px}
  .t4 .name{left:52px;top:28px;font-size:30px;letter-spacing:-1px}
  .t4 .method{left:190px;top:84px;font-size:18px;color:var(--white);font-weight:800;letter-spacing:1px}
  .t4 .copy{left:27px;font-size:24px;color:var(--white);font-family:'Oswald',sans-serif;font-weight:500}
  .t4 .hilite-text{left:24px;top:266px;padding:2px 5px;font-size:24px;font-weight:500;color:var(--red);background:var(--gold-sheen);border-radius:3px}

  /* tile 5 */
  .t5 .the{left:0;width:169px;top:200px;text-align:center;font-size:11px;color:var(--white)}
  .t5 .name1{left:0;width:169px;top:220px;text-align:center;font-size:22px;color:var(--gold)}
  .t5 .name2{left:0;width:169px;top:246px;text-align:center;font-size:35px;color:var(--gold)}
  .t5 .method{left:0;width:169px;top:290px;text-align:center;font-size:13px;color:#bbb}
  .t5 .divider{left:169px;top:198px;width:1px;height:128px;background:#666}
  .t5 .copy{left:193px;top:211px;font-size:21px;color:var(--white);font-family:'Oswald',sans-serif;font-weight:700;line-height:1.02}

  /* tile 6 */
  .t6 .band-text{left:24px;top:108px;font-size:30px;color:var(--black);transform:rotate(-20deg);transform-origin:left top;line-height:.98}
  .t6 .copy{left:28px;top:181px;font-size:25px;color:var(--white);font-family:'Oswald',sans-serif;font-weight:500;line-height:1.1}
</style>
</head>
<body>
<main class="canvas">

  <!-- Graphic 1: text only -->
  <section class="tile t1" aria-label="Fast-track graphic, text only">
    <svg class="abs" width="349" height="349" viewBox="0 0 349 349">
      <defs>
        <linearGradient id="sheen1" x1="0" x2="1" y1="0" y2="0">
          <stop offset="0" stop-color="#b8862a"/><stop offset=".35" stop-color="#f6e7a1"/>
          <stop offset=".65" stop-color="#c9972e"/><stop offset="1" stop-color="#f2dc8a"/>
        </linearGradient>
      </defs>
      <path d="M0 0 H349 V30 Q175 95 0 37 Z" fill="url(#sheen1)"/>
      <path d="M0 349 V322 Q175 270 349 310 V349 Z" fill="url(#sheen1)"/>
    </svg>
    <p class="abs kicker">THE LANTERN RIDGE METHOD</p>
    <p class="abs cond h-fast">FAST-TRACK</p>
    <p class="abs h-way oswald">YOUR WAY TO A</p>
    <p class="abs cond h-multi">MULTI-MILLION</p>
    <p class="abs cond h-biz">BUSINESS!</p>
    <div class="btn btn-red" style="left:115px;top:285px;height:28px;font-size:18px">SIGN UP TODAY!</div>
    <svg class="cursor" style="left:219px;top:305px" viewBox="0 0 16 20"><path d="M1 1V16L5 12L8 19L10.5 18L7.5 11H13Z" fill="#000" stroke="#fff"/></svg>
  </section>

  <!-- Graphic 2 -->
  <section class="tile t2" aria-label="Graphic with course hosts over night sky">
    <div class="photo" role="img" aria-label="Background of red and purple fireworks in a night sky" style="inset:0;background:radial-gradient(circle at 70% 35%,#7a2a8a 0%,#3a1b6a 30%,var(--navy) 70%),var(--navy)"></div>
    <div class="photo" role="img" aria-label="Photo of the two course hosts, a man in a black turtleneck and a woman in a denim blazer" style="left:0;top:83px;width:237px;height:266px;background:linear-gradient(180deg,#3a2a3a 0%,#1f2440 55%,#18223e 100%);border-radius:60px 90px 0 0"></div>
    <p class="abs mont the">THE</p>
    <p class="abs mont name gold-text">LANTERN RIDGE</p>
    <p class="abs mont method">METHOD</p>
    <p class="abs mont sub">How to Create a<br>7-Figure Business<br>From Scratch</p>
    <div class="btn btn-gold" style="right:25px;top:294px;height:23px;font-size:14px">SIGN UP TODAY!</div>
    <svg class="cursor" style="left:316px;top:313px" viewBox="0 0 16 20"><path d="M1 1V16L5 12L8 19L10.5 18L7.5 11H13Z" fill="#fff" stroke="#000"/></svg>
  </section>

  <!-- Graphic 3 -->
  <section class="tile t3" aria-label="Title card graphic">
    <div class="abs panel"></div>
    <p class="abs mont the">The</p>
    <p class="abs mont word" style="top:96px">Lantern</p>
    <p class="abs mont word" style="top:148px">Ridge</p>
    <p class="abs mont method">Method</p>
    <p class="abs sub">How to Create a 7-Figure<br>Business From Scratch</p>
    <div class="btn btn-gold" style="right:43px;top:302px;height:28px;font-size:16px">SIGN UP TODAY!</div>
    <svg class="cursor" style="left:298px;top:322px" viewBox="0 0 16 20"><path d="M1 1V16L5 12L8 19L10.5 18L7.5 11H13Z" fill="var(--red)" stroke="#000"/></svg>
  </section>

  <!-- Graphic 4 -->
  <section class="tile t4" aria-label="Graphic with hosts and rings">
    <svg class="abs" width="349" height="349" viewBox="0 0 349 349">
      <defs>
        <linearGradient id="sheen4" x1="0" x2="1" y1="0" y2="1">
          <stop offset="0" stop-color="#f6e7a1"/><stop offset=".5" stop-color="#b8862a"/><stop offset="1" stop-color="#f2dc8a"/>
        </linearGradient>
      </defs>
      <circle cx="62" cy="148" r="37" fill="none" stroke="var(--red)" stroke-width="20"/>
      <circle cx="294" cy="211" r="30" fill="none" stroke="url(#sheen4)" stroke-width="18"/>
    </svg>
    <div class="photo" role="img" aria-label="Photo of the two course hosts smiling, arms crossed" style="left:56px;top:75px;width:248px;height:200px;background:linear-gradient(180deg,#3b2a26 0%,#1c2233 60%,#12182a 100%);border-radius:70px 80px 0 0"></div>
    <p class="abs oswald the">THE</p>
    <p class="abs mont name gold-text">LANTERN RIDGE</p>
    <p class="abs mont method">METHOD</p>
    <p class="abs copy" style="top:236px">HOW TO CREATE A</p>
    <p class="abs oswald hilite-text">7-FIGURE BUSINESS</p>
    <p class="abs copy" style="top:302px">FROM SCRATCH</p>
    <div class="btn btn-red" style="left:244px;top:299px;height:20px;font-size:12px">SIGN UP TODAY!</div>
    <svg class="cursor" style="left:314px;top:315px" viewBox="0 0 16 20"><path d="M1 1V16L5 12L8 19L10.5 18L7.5 11H13Z" fill="#000" stroke="#fff"/></svg>
  </section>

  <!-- Graphic 5 -->
  <section class="tile t5" aria-label="Graphic with hosts over gold background">
    <div class="photo" role="img" aria-label="Gold background with faint floating banknotes" style="inset:0;background:linear-gradient(120deg,#c9972e 0%,#f6e7a1 45%,#d8b24a 100%)"></div>
    <div class="photo" role="img" aria-label="Photo of the two course hosts smiling, a woman in pink and a man in a black jacket" style="left:24px;top:9px;width:312px;height:190px;background:linear-gradient(180deg,#5a3b2e 0%,#7a2a3c 55%,#1e1e22 100%);border-radius:90px 90px 0 0"></div>
    <svg class="abs" width="349" height="349" viewBox="0 0 349 349">
      <path d="M0 206 Q150 160 349 168 V349 H0 Z" fill="var(--black)"/>
      <path d="M0 206 Q150 160 349 168" fill="none" stroke="var(--white)" stroke-width="6"/>
    </svg>
    <p class="abs mont the">— THE —</p>
    <p class="abs mont name1">LANTERN</p>
    <p class="abs mont name2">RIDGE</p>
    <p class="abs mont method">METHOD</p>
    <div class="abs divider"></div>
    <p class="abs copy">How to Create<br>a 7-Figure<br>Business From<br>Scratch</p>
    <div class="btn btn-red" style="left:195px;top:302px;height:20px;font-size:13px">SIGN UP TODAY!</div>
    <svg class="cursor" style="left:285px;top:316px" viewBox="0 0 16 20"><path d="M1 1V16L5 12L8 19L10.5 18L7.5 11H13Z" fill="#fff" stroke="var(--red)"/></svg>
  </section>

  <!-- Graphic 6 -->
  <section class="tile t6" aria-label="Graphic with diagonal gold band">
    <div class="photo" role="img" aria-label="Photo of the two course hosts, a woman in pink with arms crossed and a man in a black jacket" style="left:136px;top:109px;width:213px;height:240px;background:linear-gradient(180deg,#4a2e28 0%,#b8334a 50%,#1a1a1c 100%);border-radius:80px 80px 0 0"></div>
    <svg class="abs" width="349" height="349" viewBox="0 0 349 349">
      <defs>
        <linearGradient id="sheen6" x1="0" x2="1" y1="0" y2="0">
          <stop offset="0" stop-color="#b8862a"/><stop offset=".4" stop-color="#f6e7a1"/>
          <stop offset=".7" stop-color="#c9972e"/><stop offset="1" stop-color="#f2dc8a"/>
        </linearGradient>
      </defs>
      <path d="M58 30 L150 0 H200 L64 48 Z" fill="var(--red)"/>
      <path d="M0 84 L240 0 H349 V58 L0 178 Z" fill="url(#sheen6)"/>
      <path d="M0 178 L349 58 V66 L0 192 Z" fill="var(--red)"/>
    </svg>
    <p class="abs cond band-text">THE LANTERN RIDGE<br>METHOD</p>
    <svg class="cursor" style="left:283px;top:56px;width:18px;height:24px" viewBox="0 0 16 20"><path d="M1 1V16L5 12L8 19L10.5 18L7.5 11H13Z" fill="#fff" stroke="#000"/></svg>
    <p class="abs copy">FAST TRACK<br>YOUR WAY TO A<br>MULTI-MILLION<br>BUSINESS!</p>
    <div class="btn btn-gold" style="left:30px;top:299px;height:23px;font-size:15px">SIGN UP TODAY!</div>
  </section>

</main>
</body>
</html>
```